Label Design for honey from a small farm in Italy

We need a label for our Acacia's honey .
We are a little farm in Italy and we would like something like organic, raw and simple.
Maybe with botanical drawing with different color like watercolor o something like that (very important natural and easy)
the jar for 1kg of honey: Capacity: 780 ml - Height: 137 mm - Diameter: ∅ 94 mm
- size approx h 5,5 x 10/14cm ( we use the same label for kg and 500 gr jar)

Industry/Entity Type

Farm

Requirements
Must have
• the writings:
- Acacia
- Miele italiano di Acacia
- Da consumarsi preferibilmente entro: ( and below the space to put the date by the hands)
- some space to put some presentation of the farm or some phrases
- our logo
- the space to put the weight by the hands
- Prodotto da Azienda Agricola ...(produced by Farm Name and address....)
- Confezionato presso Apicoltura... (packaged at apiculture Name and address..)
- graphic of Acacia’s flowers ( like drawing)
Should not have
• Barcode
nutritional table

```html
<!DOCTYPE html>
<html lang="it">
<head>
<meta charset="utf-8">
<title>Miele Italiano di Acacia – Etichetta</title>
<link rel="stylesheet" href="https://fonts.googleapis.com/css2?family=Josefin+Sans:wght@600;700&family=Playfair+Display:ital,wght@1,400&family=Special+Elite&family=Caveat:wght@400&display=swap">
<style>
  :root {
    --paper: #d4e0bc;
    --olive: #34420f;
    --acacia-green: #2f8a17;
    --ink-red: #e0452c;
    --muted: #5f6d44;
    --leaf-dark: #3e6a2a;
    --leaf-light: #b9cc9c;
    --faint: rgba(52, 66, 15, 0.12);
  }
  * { margin: 0; padding: 0; box-sizing: border-box; }
  html, body { width: 1200px; height: 424px; overflow: hidden; background: var(--paper); }
  .label { position: relative; width: 1200px; height: 424px; background: var(--paper); color: var(--olive); }

  .headline {
    position: absolute; left: 0; right: 0; top: 24px; text-align: center;
    font-family: "Josefin Sans", sans-serif; font-weight: 700; font-size: 20px;
    letter-spacing: 0.36em; color: var(--olive); padding-left: 0.36em;
  }
  .botanical {
    position: absolute; left: 514px; top: 57px; width: 173px; height: 218px;
    border-radius: 40% 45% 20% 30%;
    background: radial-gradient(ellipse at 45% 45%, var(--leaf-dark) 0%, #6f9a57 45%, var(--leaf-light) 75%, rgba(212,224,188,0) 100%);
  }
  .product-name {
    position: absolute; left: 512px; top: 232px; width: 176px; text-align: center;
    font-family: "Josefin Sans", sans-serif; font-weight: 700; font-size: 38px;
    letter-spacing: 0.16em; color: var(--acacia-green); padding-left: 0.16em;
  }
  .botanical-note {
    position: absolute; left: 708px; top: 245px;
    font-family: "Special Elite", monospace; font-size: 8px; line-height: 12px; color: var(--muted);
  }
  .intro {
    position: absolute; top: 91px; width: 170px;
    font-family: "Playfair Display", serif; font-style: italic; font-size: 13.5px;
    line-height: 17.9px; letter-spacing: -0.03em; color: var(--olive);
  }
  .intro--left { left: 74px; text-align: left; }
  .intro--right { left: 959px; text-align: right; }

  .brand-mark-faint {
    position: absolute; left: 1060px; top: 322px; transform: rotate(-90deg); transform-origin: left top;
    font-family: "Josefin Sans", sans-serif; font-weight: 700; font-size: 26px;
    color: var(--faint); letter-spacing: 0.04em; white-space: nowrap;
  }
  .brand-mark-faint { left: 1098px; top: 396px; }

  .info-table { position: absolute; left: 243px; top: 277px; width: 716px; height: 123px; border: 5px solid var(--olive); }
  .info-table .divider-v { position: absolute; top: 0; bottom: 0; width: 3px; background: var(--olive); }
  .info-table .divider-h { position: absolute; height: 2px; background: var(--olive); }

  .brand-cell {
    position: absolute; left: 0; top: 0; width: 139px; height: 100%;
    display: flex; align-items: center; justify-content: center; gap: 6px;
    font-family: "Josefin Sans", sans-serif; font-weight: 700; font-size: 13px; color: var(--olive); letter-spacing: 0.02em;
  }
  .brand-cell .brand-square { width: 8px; height: 8px; background: var(--olive); }

  .typed { position: absolute; font-family: "Special Elite", monospace; font-size: 8.4px; color: var(--olive); white-space: nowrap; letter-spacing: 0.02em; }
  .typed--bold { font-size: 11px; font-weight: 700; }
  .typed--red { color: var(--ink-red); font-size: 13px; letter-spacing: 0.05em; }
  .handwritten { position: absolute; font-family: "Caveat", cursive; color: var(--ink-red); white-space: nowrap; }
</style>
</head>
<body>
<main class="label">
  <h1 class="headline">MIELE ITALIANO</h1>

  <div class="botanical" role="img" aria-label="Illustrazione botanica ad acquerello di un ramo di acacia con foglie verdi e grappoli di fiori bianchi"></div>

  <h2 class="product-name">ACACIA</h2>
  <p class="botanical-note">Hl'acacia,nome scientifico<br>Robinia Pseudoacacia L.</p>

  <p class="intro intro--left">Il miele di acacia è molto conosciuto&nbsp; e apprezzato per le sue caratteristiche, che lo rendono appetibile anche a coloro che non mal sopportano i sapori più forti e particolari. Le sue particolarità iniziano già dal colore.</p>
  <p class="intro intro--right">Il miele di acacia è molto conosciuto&nbsp; e apprezzato per le sue caratteristiche, che lo rendono appetibile anche a coloro che non mal sopportano i sapori più forti e particolari. Le sue particolarità iniziano già dal colore.</p>

  <div class="brand-mark-faint" aria-hidden="true">IL POGGIOLO</div>

  <section class="info-table">
    <div class="brand-cell"><span class="brand-square"></span>IL POGGIOLO</div>
    <span class="divider-v" style="left:139px"></span>
    <span class="divider-v" style="left:563px"></span>
    <span class="divider-h" style="left:142px; right:0; top:37px"></span>
    <span class="divider-h" style="left:142px; right:0; top:72px"></span>

    <span class="typed" style="left:161px; top:13px">Smielato e confezionato presso</span>
    <span class="typed" style="left:213px; top:28px">Apicoltura Bellandi Marco Via Oleandri 17, 21100 Varese</span>
    <span class="typed" style="left:162px; top:47px">Prodotto da Azienda Agricola Il Poggiolo</span>
    <span class="typed" style="left:213px; top:64px">Società Semplice di</span>
    <span class="handwritten" style="left:350px; top:54px; font-size:17px">Moretti L</span>
    <span class="typed" style="left:439px; top:64px">e</span>
    <span class="handwritten" style="left:454px; top:54px; font-size:17px">Galli R</span>
    <span class="typed" style="left:160px; top:100px">Da consumarsi preferibilmente entro il</span>
    <span class="handwritten" style="left:437px; top:85px; font-size:24px">10-10-22</span>

    <span class="typed typed--bold" style="left:576px; top:10px">PI:</span>
    <span class="typed typed--red" style="left:595px; top:25px">04812360197</span>
    <span class="typed" style="left:576px; top:49px">Via dei Tigli 14, 21012,</span>
    <span class="typed" style="left:581px; top:61px">Borgo Lieto (Va)</span>
    <span class="typed typed--bold" style="left:574px; top:99px">Peso</span>
    <span class="handwritten" style="left:627px; top:80px; font-size:27px">475 gr</span>
  </section>
</main>
</body>
</html>
```